Website Banner Redesign for Kelbra Gearbin Centre

Business Name:
KELBRA GEARBIN CENTRE

About Us:
- We’re a proudly Australian company that designs and builds tough, reliable toolboxes for Utes, Trucks, and Campervans. Our products are made to handle harsh conditions and are trusted by tradies, off-roaders, and professional fleets across the country.

Project Goal:
- We want to refresh our homepage and category banners with bold, modern designs that better showcase our products and value proposition.

Why We’re Updating:
Our current banners show the products well, but we want to improve:
Visual impact and hierarchy
- Readability of text (especially on mobile)
- Clearer calls-to-action (CTAs)
- Brand messaging around “Built Tough”, “Aussie Made”, and “Custom Fit-Outs”

Target Audience:
- Tradespeople
- 4x4 & off-road enthusiasts
- Caravan & camping community
- Ute/Truck/Caravan dealerships
- Fleet and commercial buyers

Design Style We Want:
- Bold, confident, rugged
- Clean layout with clear focal points
- Strong product imagery (we’ll supply photos)
- Use of brand colors: Black, White, Red, Grey
- Professional, not too busy or cluttered

Banner Uses:
- Homepage hero banner
- Category landing pages

UTE TOOLBOXES - https://www.kelbragearbin.com.au/aluminium-toolboxes/
Truck Boxes - https://www.kelbragearbin.com.au/truck-toolboxes/
Canopies - https://www.kelbragearbin.com.au/canopy/
Dog Boxes - https://www.kelbragearbin.com.au/dog-boxes/
CAMPER BOXES - https://www.kelbragearbin.com.au/camper-toolboxes/
Accessories - https://www.kelbragearbin.com.au/accessories/

- Can be reused for desktop and mobile

Inspiration Style:
Think: 4x4 accessory brands, tough tradie gear, or clean eCommerce landing banners from premium auto suppliers.

Target Market(s)

All in Brief Above

Industry/Entity Type

Retail

Requirements
Must have
• A banner using our products only. A banner for each category, and 2 alternate banners for the home page.
Nice to have
• I have added some designs which i like..... Please take a look and take inspiration from them.

```html
<!DOCTYPE html>
<html lang="en">
<head>
<meta charset="utf-8">
<title>Dog Boxes Banner</title>
<link rel="stylesheet" href="https://fonts.googleapis.com/css2?family=Anton&display=swap">
<style>
  :root {
    --bg-deep: #1b252c;
    --bg-mid: #34434d;
    --headline: #ffffff;
    --accent-yellow: #ffd200;
    --cta: #a81d4b;
    --cta-text: #ffffff;
    --product-light: #f4f5f5;
    --product-shade: #d9dcde;
  }
  html, body {
    margin: 0;
    padding: 0;
    width: 900px;
    height: 1200px;
    overflow: hidden;
  }
  .banner {
    position: relative;
    width: 900px;
    height: 1200px;
    overflow: hidden;
    font-family: "Anton", "Oswald", sans-serif;
    background:
      radial-gradient(ellipse 420px 320px at 50% 56%, rgba(190,205,212,0.55), transparent 70%),
      radial-gradient(ellipse 500px 380px at 45% 22%, rgba(120,140,150,0.45), transparent 70%),
      radial-gradient(ellipse 600px 500px at 85% 90%, rgba(10,15,20,0.6), transparent 70%),
      linear-gradient(160deg, var(--bg-mid) 0%, var(--bg-deep) 60%, #141c22 100%);
  }
  .headline {
    position: absolute;
    left: 65px;
    top: 66px;
    margin: 0;
    color: var(--headline);
    font-size: 150px;
    line-height: 144px;
    font-weight: 400;
    text-transform: uppercase;
    letter-spacing: -3px;
  }
  .product-image {
    position: absolute;
    left: 223px;
    top: 500px;
    width: 465px;
    height: 312px;
    border-radius: 4px;
    background: linear-gradient(120deg, var(--product-light) 0%, #ffffff 40%, var(--product-shade) 100%);
    box-shadow: 0 0 60px 20px rgba(200,215,222,0.45);
  }
  .subline {
    position: absolute;
    left: 69px;
    top: 816px;
    margin: 0;
    color: var(--accent-yellow);
    font-size: 72px;
    line-height: 79px;
    font-weight: 400;
    text-transform: uppercase;
    letter-spacing: 0.7px;
  }
  .cta-button {
    position: absolute;
    left: 65px;
    top: 1015px;
    width: 527px;
    height: 125px;
    border-radius: 18px;
    background: var(--cta);
    color: var(--cta-text);
    text-decoration: none;
    display: flex;
    align-items: center;
    justify-content: center;
    font-size: 82px;
    line-height: 1;
    text-transform: uppercase;
    letter-spacing: 0;
  }
</style>
</head>
<body>
  <main class="banner">
    <h1 class="headline">Safe &amp;<br>Comfortable<br>Dog Boxes</h1>
    <div class="product-image" role="img" aria-label="White steel canopy-style dog box with a locking front door and mesh vent on the side"></div>
    <p class="subline">Designed for your canine<br>companion's safety</p>
    <a class="cta-button" href="/dog-boxes/">Shop Dog Box</a>
  </main>
</body>
</html>
```